lunetra.com redesign

We are a successful web hosting company that has been around since 1999 with 10,000 customers managing 2,000 websites and 12,000 domain names. Our challenge - we are losing ground because our site is getting old, our pricing is not competitive and our feature set needs to change to match the new world of mobile centric everything. We want to reach out to all of the domain names that we don't host websites for. We believe that if we designed a new site that focuses on bringing home all of those externally hosted websites to our own web hosting company that we would have a solid future. We need to compete against mopwizzle.com, vantrimble.com, kerbloom.com, zinqhut.com, nolvark.com, brimfolk.com, quorvane.com, welbix.com and 100,000 others. We need to simplify our message with clean design, focused pages, easy decision making processes for the consumer. We use WHMCS for the background provisioning and billing so we can pretty much manage any kind of pricing model and discounted promotion packages.
I would prefer Twitter bootstrap CSS based responsive design.

Reason: I was away on vacation for 2 weeks - I just got back - I need time to fairly review all submissions - thank you for your patience. Dorian Fenwick Lunetra.com

Thanks to all who submitted sample designs - unfortunately most of them were nothing much more than already available templates with some of my current content and logo added to them. I will try to be more specific to reduce the number of choices. I need the template be fully compatible with WHMCS and Wordpress if you can't make it work with WHMCS directly. Another question I have to ask is -"exactly what am I getting for my $500.00 - is it just a PSD template or actual integration of that theme into WHMCS or Wordpress?"  I don't expect anyone to create new content for the site at that price. What do you charge if  you are able to create content or get directly involved in the site implementation of that template?

```html
<!DOCTYPE html>
<html lang="en">
<head>
<meta charset="utf-8">
<title>Lunetra — Domains &amp; Web Hosting</title>
<link rel="stylesheet" href="https://fonts.googleapis.com/css2?family=Roboto:wght@300;400;500;700&family=Arimo:wght@400;700&display=swap">
<style>
:root{
  --ink:#1c1c1c;
  --text:#333;
  --muted:#8a8a8a;
  --brand:#1a5b8a;
  --brand-dark:#0f4a75;
  --green:#6a9e1f;
  --tick:#5e9a1e;
  --topbar:#1e1e1e;
  --band:rgba(18,18,18,.78);
  --rule:#dcdcdc;
  --light:#f6f6f6;
  --grey:#efefef;
  --footer:#d9d9d9;
  --white:#fff;
}
*{box-sizing:border-box;margin:0;padding:0}
html,body{width:1200px;height:2460px;overflow:hidden}
body{position:relative;background:var(--white);font-family:"Roboto",Arial,sans-serif;color:var(--text)}

/* top bar */
.topbar{position:absolute;left:0;top:0;width:1200px;height:38px;background:var(--topbar);font-size:10px;color:#ddd}
.utility-links{position:absolute;left:150px;top:13px;display:flex;gap:16px}
.login{position:absolute;left:643px;top:9px;display:flex;align-items:center;gap:6px}
.login .field{width:112px;height:19px;background:#fff;color:#555;font-size:10px;padding:3px 5px}
.login .btn{height:19px;background:var(--brand);color:#fff;font-size:10px;padding:3px 7px}
.cart{position:absolute;left:975px;top:10px;display:flex;align-items:center;gap:8px;font-size:13px;color:#fff}

/* hero */
.hero{position:absolute;left:0;top:38px;width:1200px;height:517px;background:linear-gradient(180deg,#c7d1da 0%,#b3c1cd 35%,#93a5b6 65%,#6b7d90 100%)}
.brand{position:absolute;left:150px;top:58px;font-size:42px;font-weight:700;color:#fff;letter-spacing:-1px}
.main-nav{position:absolute;left:452px;top:72px;display:flex;font-size:12.5px;font-weight:500;color:#fff}
.main-nav span{margin-right:30px}
.dropdown{position:absolute;left:513px;top:98px;width:143px;height:166px;background:#fff;padding:5px 8px;font-size:9.5px;line-height:16.4px;color:#444;box-shadow:0 2px 6px rgba(0,0,0,.2);list-style:none}
.hero-title{position:absolute;left:0;top:214px;width:1200px;text-align:center;font-size:62px;font-weight:300;color:var(--ink);letter-spacing:-1px}
.hero-sub{position:absolute;left:0;top:273px;width:1200px;text-align:center;font-size:25px;font-weight:500;color:#12395a}
.hero-copy{position:absolute;left:0;top:313px;width:1200px;text-align:center;font-size:13px;line-height:17px;color:#1c1c1c}
.start{position:absolute;left:550px;top:364px;width:88px;height:27px;background:#fafafa;border:1px solid #ccc;font-size:14px;font-weight:700;color:#222;text-align:center;line-height:25px}
.arrow{position:absolute;top:250px}

/* domain search */
.search-band{position:absolute;left:0;top:469px;width:1200px;height:86px;background:var(--band);color:#fff}
.search-band h2{position:absolute;left:224px;top:18px;font-size:29px;font-weight:500}
.search-band .hint{position:absolute;left:225px;top:54px;font-size:12px}
.search-form{position:absolute;left:603px;top:20px;display:flex;height:28px}
.search-form .www{width:57px;background:#e8e8e8;color:#333;font-size:15px;font-weight:500;line-height:28px;text-align:center}
.search-form .input{width:235px;background:#fff;color:#aaa;font-size:10px;line-height:28px;padding-left:6px}
.search-form .go{width:80px;background:var(--brand);color:#fff;font-size:14px;font-weight:500;line-height:28px;text-align:center}
.sale{position:absolute;left:603px;top:57px;font-size:13px}

/* pricing */
.section-title{position:absolute;left:0;width:1200px;text-align:center;font-weight:300}
.pricing{position:absolute;left:225px;top:681px;width:750px;table-layout:fixed;border-collapse:collapse;font-size:12.5px;color:var(--muted);text-align:center;font-weight:300}
.pricing col{width:150px}
.pricing th{height:32px;background:var(--brand-dark);color:#fff;font-weight:400;font-size:13px;border-right:1px solid #3d6d92}
.pricing td{height:34px;border:1px solid var(--rule)}
.pricing tr:last-child td{height:25px}
.pricing .gap{border-top:none;border-bottom:none;background:transparent}
.choose{display:inline-block;width:58px;height:16px;background:var(--brand-dark);color:#fff;font-size:10.5px;line-height:16px;font-weight:400}
.featured{position:absolute;left:676px;top:664px;width:150px;height:229px;background:#fff;box-shadow:0 0 8px rgba(0,0,0,.22);text-align:center;font-size:13px;color:#333}
.featured .head{height:49px;background:var(--green);color:#fff;font-size:14px;line-height:52px}
.featured .cell{height:37.5px;line-height:37.5px;border-bottom:1px solid var(--rule)}
.featured .choose{background:var(--green)}
.divider{position:absolute;left:225px;top:951px;width:750px;height:1px;background:#e3e3e3}

/* features */
.portrait{position:absolute;left:262px;top:984px;width:282px;height:287px;background:radial-gradient(ellipse at 50% 45%,#e9d4c2 0%,#d3b293 35%,#f4f4f4 72%)}
.feature{position:absolute;left:606px}
.feature svg{position:absolute;left:0;top:2px}
.feature h3{margin-left:32px;font-size:14.5px;font-weight:500;color:var(--brand)}
.feature p{margin-left:32px;font-size:11.5px;color:#666;margin-top:2px}

/* free services */
.services{position:absolute;left:0;top:1271px;width:1200px;height:353px;background:var(--light)}
.services h2{position:absolute;left:0;top:36px;width:1200px;text-align:center;font-size:27px;font-weight:400;color:#111;line-height:29px}
.services h2 em{font-style:normal;color:var(--brand)}
.service{position:absolute;top:145px;width:190px;text-align:center}
.service h4{font-size:13.5px;font-weight:500;color:var(--brand)}
.service svg{display:block;margin:18px auto 14px}
.service p{width:136px;margin:0 auto;font-family:"Arimo",Arial,sans-serif;font-size:11px;line-height:15px;color:#555}

/* about grid */
.about{position:absolute;left:0;top:1624px;width:1200px;height:697px;background:var(--grey)}
.about h2{position:absolute;left:0;top:45px;width:1200px;text-align:center;font-size:27px;font-weight:400;color:var(--brand);line-height:29px}
.grid{position:absolute;left:225px;top:154px;width:750px;display:grid;grid-template-columns:repeat(4,1fr)}
.card{padding:14px 20px 10px;border-right:1px solid #fff;border-bottom:1px solid #fff;font-family:"Arimo",Arial,sans-serif;font-size:9.6px;line-height:13.2px;color:#111;text-align:justify}
.card:nth-child(4n){border-right:none}
.card.r1{height:210px}
.card.r2{height:318px;border-bottom:none}
.card h4{font-family:"Roboto",Arial,sans-serif;font-size:13px;font-weight:500;color:#16456b;text-align:center;margin-bottom:13px;line-height:15px}
.card p+p{margin-top:13px}
.badge{display:block;margin:0 auto 30px}

/* footer */
.footer{position:absolute;left:0;top:2321px;width:1200px;height:139px;background:var(--footer);font-family:"Arimo",Arial,sans-serif;font-size:9.5px;color:#111;text-align:center}
.footer .links{position:absolute;top:22px;width:1200px}
.footer .copy{position:absolute;top:37px;width:1200px}
.payments{position:absolute;left:551px;top:64px;display:flex;gap:3px}
.payments span{width:30px;height:17px;border-radius:2px}
.footer .fine{position:absolute;top:93px;width:1200px;line-height:14px}
.to-top{position:absolute;left:1015px;top:2384px;width:34px;height:34px;border-radius:4px;background:#1f5f8f}
</style>
</head>
<body>

<header class="topbar">
  <nav class="utility-links"><span>Company</span><span>Partners</span><span>Support</span><span>Contact Us</span><span>References</span><span>Pricing</span></nav>
  <div class="login"><span>Login</span><span class="field">user name</span><span class="field">password</span><span class="btn">Login</span></div>
  <div class="cart">
    <svg width="18" height="15" viewBox="0 0 18 15"><path d="M1 1h3l2 9h9l2-6H5" fill="none" stroke="#fff" stroke-width="1.6"/><circle cx="7" cy="13" r="1.4" fill="#fff"/><circle cx="14" cy="13" r="1.4" fill="#fff"/></svg>
    View Cart
  </div>
</header>

<section class="hero" role="img" aria-label="Blurred city skyline photograph with tall towers under a pale sky"></section>

<div class="brand">lunetra</div>
<nav class="main-nav">
  <span>Home</span><span>Domain Name Center</span><span>Web Site Hosting Center</span><span>S.E.O. Toolkit</span><span>Support</span><span>Client Area</span>
</nav>

<h1 class="hero-title">Free domain name</h1>
<p class="hero-sub">with every new hosting package.</p>
<p class="hero-copy">Sign up for one of our affordable hosting packages,<br>and your top-level domain is on us</p>
<div class="start">Start Now</div>
<svg class="arrow" style="left:276px" width="20" height="36" viewBox="0 0 20 36"><path d="M17 2 3 18l14 16" fill="none" stroke="#333" stroke-width="2.5"/></svg>
<svg class="arrow" style="left:914px" width="20" height="36" viewBox="0 0 20 36"><path d="M3 2l14 16L3 34" fill="none" stroke="#333" stroke-width="2.5"/></svg>

<ul class="dropdown">
  <li>Expired Domain Name Search</li><li>Domain Pricing</li><li>Domain Transfers</li><li>Domain Renewal</li><li>Account Management</li><li>ID Protect</li><li>Free Domain Forwarding</li><li>Free Email Forwarding</li><li>Domain Law Issues</li><li>Trademark Search</li>
</ul>

<section class="search-band">
  <h2>Find your domain name !</h2>
  <p class="hint">Enter a Domain Name</p>
  <div class="search-form"><span class="www">www.</span><span class="input">Your-name.com</span><span class="go">Search</span></div>
  <p class="sale"><b>Sale!</b> Premium top-level domain names from $15/year.</p>
</section>

<h2 class="section-title" style="top:600px;font-size:23px;color:#444">Choose A Hosting Package</h2>

<table class="pricing">
  <colgroup><col><col><col><col><col></colgroup>
  <tr><th></th><th>e-Lite</th><th>e-200</th><th></th><th>e-1000</th></tr>
  <tr><td>Storage</td><td>100 Mb</td><td>200 Mb</td><td class="gap"></td><td>1000 Mb</td></tr>
  <tr><td>Domain Name</td><td>Included</td><td>Included</td><td class="gap"></td><td>Included</td></tr>
  <tr><td>eMail Accounts</td><td>Unlimited</td><td>Unlimited</td><td class="gap"></td><td>Unlimited</td></tr>
  <tr><td>Annual Price</td><td>$90</td><td>$149</td><td class="gap"></td><td>$549</td></tr>
  <tr><td></td><td><span class="choose">Choose</span></td><td><span class="choose">Choose</span></td><td class="gap"></td><td><span class="choose">Choose</span></td></tr>
</table>

<div class="featured">
  <div class="head">e-500</div>
  <div class="cell">500 Mb</div>
  <div class="cell">Included</div>
  <div class="cell">Unlimited</div>
  <div class="cell">$249</div>
  <div class="cell" style="border:none;line-height:30px"><span class="choose">Choose</span></div>
</div>

<div class="divider"></div>

<div class="portrait" role="img" aria-label="Photograph of a smiling businesswoman in a dark blazer with arms crossed"></div>

<div class="feature" style="top:1005px">
  <svg width="22" height="18" viewBox="0 0 22 18"><path d="M2 9l6 6L20 2" fill="none" stroke="var(--tick)" stroke-width="3.5"/></svg>
  <h3>Secure Your Domain Name</h3><p>Register, renew, transfer or search your domain name</p>
</div>
<div class="feature" style="top:1064px">
  <svg width="22" height="18" viewBox="0 0 22 18"><path d="M2 9l6 6L20 2" fill="none" stroke="var(--tick)" stroke-width="3.5"/></svg>
  <h3>Effective Website Development</h3><p>StackPages Web Builder, Small Business Bundle and Custom Design</p>
</div>
<div class="feature" style="top:1121px">
  <svg width="22" height="18" viewBox="0 0 22 18"><path d="M2 9l6 6L20 2" fill="none" stroke="var(--tick)" stroke-width="3.5"/></svg>
  <h3>Web Site Hosting</h3><p>Reliable, affordable options, Real People - real support</p>
</div>
<div class="feature" style="top:1179px">
  <svg width="22" height="18" viewBox="0 0 22 18"><path d="M2 9l6 6L20 2" fill="none" stroke="var(--tick)" stroke-width="3.5"/></svg>
  <h3>Market Your Web Site</h3><p>Professional implementation of Search Engine Positioning</p>
</div>

<section class="services">
  <h2>Get these free services and many more<br><em>with all accounts</em></h2>
  <div class="service" style="left:224px">
    <h4>Easy Transfer</h4>
    <svg width="52" height="36" viewBox="0 0 52 36"><rect x="4" y="14" width="44" height="18" fill="none" stroke="#333" stroke-width="1.5"/><path d="M26 26V4M19 11l7-7 7 7" fill="none" stroke="#333" stroke-width="1.5"/></svg>
    <p>Switching to Lunetra from another host is easy: sit back while we take care of everything.</p>
  </div>
  <div class="service" style="left:411px">
    <h4>Site Builder</h4>
    <svg width="52" height="36" viewBox="0 0 52 36"><rect x="6" y="3" width="40" height="30" fill="none" stroke="#333" stroke-width="1.5"/><path d="M6 9h40M12 14h12v13H12zM28 14h12M28 19h12M28 24h12" fill="none" stroke="#333" stroke-width="1.5"/></svg>
    <p>With SiteBuilder, you can build your website with drag-and-drop simplicity.</p>
  </div>
  <div class="service" style="left:599px">
    <h4>Installation</h4>
    <svg width="52" height="36" viewBox="0 0 52 36"><circle cx="26" cy="20" r="12" fill="none" stroke="#333" stroke-width="2"/><path d="M26 20v-7M23 4h6M26 4v4" fill="none" stroke="#333" stroke-width="2"/></svg>
    <p>Over 50 essential scripts for building your website installed in minutes with a click.</p>
  </div>
  <div class="service" style="left:786px">
    <h4>BeFound</h4>
    <svg width="52" height="36" viewBox="0 0 52 36"><path d="M8 17 44 5 34 32 26 22zM26 22l18-17" fill="none" stroke="#333" stroke-width="1.6" stroke-linejoin="round"/></svg>
    <p>We include search engine positioning with every plan, so your customers can find your website.</p>
  </div>
</section>

<section class="about">
  <h2>lunetra make it easy<br>to get online</h2>
  <div class="grid">
    <article class="card r1"><h4>About Lunetra</h4><p>As an NRCA-accredited registrar for more than 10 years, Lunetra is a leading provider of <b>domain registration, website hosting, website design, and email hosting</b> for small and medium-sized businesses. Lunetra has helped tens of thousands of businesses and individuals establish their web presence, build their websites, and drive revenue.</p></article>
    <article class="card r1"><h4>Domain Registration</h4><p><b>Registering a domain</b> is the first step in building your website. Choose from dozens of domain extensions such as .com, .net, .us, .tel, .biz, .org, .ca and .us. Lunetra offers competitive prices, easy domain search and registration, auto-renewal and domain transfers.</p></article>
    <article class="card r1"><h4>Website Hosting</h4><p>Lunetra's <b>website hosting plans</b> are fast, flexible and affordable. We offer plans to meet your varying bandwidth and disk space requirements. All web hosting plans include free setup, one-click install web applications, and SiteBuilder, our do-it-yourself website building tool. Create a strong online web presence with Lunetra hosting.</p></article>
    <article class="card r1"><h4>Email Hosting</h4><p><b>Email hosting</b> lets you create personalized email accounts at the domain of your choice. Custom email addresses are an important part of building your online brand identity and demonstrating that you are a professional, web-savvy business. Lunetra includes email hosting in all business plans.</p></article>
    <article class="card r2"><h4>SiteBuilder</h4><p>Included free with every hosting plan, Lunetra's premium <b>SiteBuilder</b> lets anyone easily create a business-quality website. Hundreds of professional templates are available.</p></article>
    <article class="card r2"><h4>Business Solutions</h4>
      <svg class="badge" width="30" height="52" viewBox="0 0 30 52"><path d="M8 26 4 50l11-6 11 6-4-24z" fill="#1d3f73"/><circle cx="15" cy="15" r="14" fill="#1d3f73"/><circle cx="15" cy="15" r="9" fill="#c9a441"/></svg>
      <p>Lunetra provides a variety of business and marketing solutions for small business customers. Some of these products include <b>Website Builder</b> and <b>Business Hosting</b> bundles and our extensive <b>Search Engine Optimization tool kit.</b></p></article>
    <article class="card r2"><h4>24/7 Customer Service</h4><p>All Lunetra products come with free 24/7 support. For more information about Lunetra customer support, visit the <b>Support</b> section of this website.</p></article>
    <article class="card r2"><h4>More Reasons to<br>Choose Lunetra</h4><p>As an award winning, premium provider of Internet services for small businesses and individuals, Lunetra offers best in class products, dedicated customer support and the highest service reliability available. Choose Lunetra and start building you website today.</p><p>Lunetra has been recognized as a leader in business <b>domain name registration and business hosting.</b> Read what others are saying about us <b>here, here and here.</b></p></article>
  </div>
</section>

<footer class="footer">
  <p class="links">Terms of Use -- Dispute Policy -- Disclaimer -- Privacy Policy -- Refund Policy -- Refund Policy -- LNET Newsletter</p>
  <p class="copy">Copyright © 2014 Lunetra.com. All Rights Reserved.</p>
  <div class="payments" aria-label="Accepted payment methods">
    <span style="background:#d8412f"></span><span style="background:#1a3f8f"></span><span style="background:#e8eef6;border:1px solid #b7c4d6"></span>
  </div>
  <p class="fine">All Transactions are based on US or Canadian Dollars. lunetra.com is registered and located in Canada<br>90 day refund guarantee on all purchases. No refunds on hosting services already provided.</p>
</footer>
<div class="to-top"><svg width="34" height="34" viewBox="0 0 34 34"><path d="M11 20l6-6 6 6" fill="none" stroke="#fff" stroke-width="2"/></svg></div>

</body>
</html>
```